The Battle of the Business Cards - Puns, Pixels, and Prizes

Briefing for Q7 Harbor Business Card Design:

Objective:
To design business cards that represent the vision and mission of Q7 Harbor, a company that aims to create the best remote work experience for people and companies, with a focus on simplicity and ease of use.

Design Elements:

Color Scheme: Blue and White
Font: Modern and Clean
Logo: The Q7 Harbor logo should be prominently displayed on the card.
Vision Statement: "Helping businesses create workplaces where people love to work" should be included on the card.
Mission Statement: "Create the best remote work experience for people and companies" should also be included.
Key Focus: The card should emphasize Q7 Harbor's focus on simplicity and ease of use in its cloud solutions.
Design Concept:
The design of the business card should be simple yet professional. The Q7 Harbor logo should be the focal point of the card, and the blue and white color scheme should be used to create a clean and modern feel that reinforces the idea of simplicity and ease of use. Blue represents trust, professionalism, and reliability, while white represents purity, simplicity, and clarity. The card should feature the vision and mission of the company, with each statement being given equal importance. The font used should be modern and clean, with legibility being a top priority. A tagline could be included that emphasizes the company's focus on simplicity and ease of use, such as "Simplicity at its best" or "Streamlined cloud solutions."

Final Thoughts:
The design of the business card should represent Q7 Harbor's vision and mission while also conveying the message that the company is the choice for those who value simplicity and ease of use in their cloud solutions. The final product should leave a lasting impression on anyone who receives it, and it should convey the professionalism and expertise of Q7 Harbor in helping businesses create workplaces where people love to work. The blue and white color scheme can be a great choice for the Q7 Harbor business card design, and it can help to create a professional and memorable impression on clients and partners while emphasizing the company's focus on simplicity and ease of use.
Updates

Need extra days to review

Target Market(s)

Companies that employ remote workers that work on computers

Industry/Entity Type

SaaS

Contact Information for Business Card

Website: www.q7harbor.net, phone, email, whatsApp, LinkedIn,

Font styles to use
Other font styles liked:
• Main Fonts: Poppins Light, Poppins Medium, Poppins Bold Alternative Fonts (for Sub Headers) Cairo Light, Cairo Regular, Cairo Bold

Colors
0054AA
0677BA
7BADD7
CADEEF
E8F1F8

Requirements
Must have
• See Copy of Q7 harbor Branding - 2021.pdf, Briefing for Q7 Harbor Business Card Design: Objective: To design business cards that represent the vision and mission of Q7 Harbor, a company that aims to create the best remote work experience for people and companies, with a focus on simplicity and ease of use. Design Elements: Color Scheme: Blue and White Font: Modern and Clean Logo: The Q7 Harbor logo should be prominently displayed on the card. Vision Statement: "Helping businesses create workplaces where people love to work" should be included on the card. Mission Statement: "Create the best remote work experience for people and companies" should also be included. Key Focus: The card should emphasize Q7 Harbor's focus on simplicity and ease of use in its cloud solutions. Design Concept: The design of the business card should be simple yet professional. The Q7 Harbor logo should be the focal point of the card, and the blue and white color scheme should be used to create a clean and modern feel that reinforces the idea of simplicity and ease of use. Blue represents trust, professionalism, and reliability, while white represents purity, simplicity, and clarity. The card should feature the vision and mission of the company, with each statement being given equal importance. The font used should be modern and clean, with legibility being a top priority. A tagline could be included that emphasizes the company's focus on simplicity and ease of use, such as "Simplicity at its best" or "Streamlined cloud solutions." Final Thoughts: The design of the business card should represent Q7 Harbor's vision and mission while also conveying the message that the company is the choice for those who value simplicity and ease of use in their cloud solutions. The final product should leave a lasting impression on anyone who receives it, and it should convey the professionalism and expertise of Q7 Harbor in helping businesses create workplaces where people love to work. The blue and white color scheme can be a great choice for the Q7 Harbor business card design, and it can help to create a professional and memorable impression on clients and partners while emphasizing the company's focus on simplicity and ease of use.
Nice to have
• Most of of our competitors treat you like a number, we give a sh!t, we take the time to help people get set up and grow. Think of the Tez vs Korvane commercials from the early 2000s

```html
<!DOCTYPE html>
<html lang="en">
<head>
<meta charset="utf-8">
<title>Q7 Harbor Business Cards</title>
<link href="https://fonts.googleapis.com/css2?family=Poppins:wght@300;400;600&family=Montserrat:wght@300;400&family=Bebas+Neue&display=swap" rel="stylesheet">
<style>
  :root {
    --backdrop: #3a3b3d;
    --card-blue: #07608f;
    --card-blue-light: #0b74a8;
    --brand-deep: #0054AA;
    --brand-mid: #0677BA;
    --brand-sky: #2a9fd8;
    --white: #ffffff;
    --paper: #ffffff;
    --tint: #E8F1F8;
  }
  * { box-sizing: border-box; margin: 0; padding: 0; }
  html, body { width: 1200px; height: 1200px; overflow: hidden; }
  body {
    background: var(--backdrop);
    position: relative;
    font-family: "Poppins", sans-serif;
  }
  .card {
    position: absolute;
    left: 180px;
    width: 840px;
    height: 480px;
    border-radius: 34px;
    overflow: hidden;
  }
  /* Front */
  .card--front {
    top: 60px;
    background: linear-gradient(120deg, var(--card-blue) 0%, var(--card-blue-light) 55%, var(--card-blue) 100%);
    color: var(--white);
  }
  .front__brand {
    position: absolute;
    left: 250px;
    top: 92px;
    font-weight: 600;
    font-size: 92px;
    letter-spacing: -1px;
    line-height: 1;
  }
  .front__contacts {
    position: absolute;
    left: 470px;
    top: 238px;
    list-style: none;
    font-family: "Montserrat", sans-serif;
    font-weight: 300;
    font-size: 21px;
    line-height: 36px;
  }
  .front__contacts li { display: flex; align-items: center; gap: 10px; }
  .front__contacts svg { width: 20px; height: 20px; flex: none; }
  .front__person {
    position: absolute;
    left: 110px;
    bottom: 80px;
    border-left: 4px solid var(--white);
    padding-left: 14px;
  }
  .person__name {
    font-family: "Montserrat", sans-serif;
    font-weight: 400;
    font-size: 42px;
    line-height: 1.05;
  }
  .person__role {
    font-family: "Montserrat", sans-serif;
    font-weight: 300;
    font-size: 21px;
    letter-spacing: 0.5px;
  }
  /* Back */
  .card--back {
    top: 640px;
    background: linear-gradient(110deg, var(--paper) 0%, var(--paper) 30%, var(--tint) 70%, var(--paper) 100%);
  }
  .back__brand {
    position: absolute;
    left: 0; right: 0;
    top: 150px;
    display: flex;
    justify-content: center;
    align-items: center;
    gap: 22px;
    color: var(--brand-mid);
    font-weight: 600;
    font-size: 80px;
    letter-spacing: -1px;
    line-height: 1;
  }
  .back__dot {
    width: 58px; height: 58px;
    border-radius: 50%;
    background: var(--brand-mid);
  }
  .back__statements {
    position: absolute;
    left: 0; right: 0;
    bottom: 70px;
    text-align: center;
    font-family: "Bebas Neue", sans-serif;
    font-size: 36px;
    line-height: 1.05;
    letter-spacing: 0.5px;
  }
  .statement--vision { color: var(--brand-mid); }
  .statement--mission { color: var(--brand-deep); }
</style>
</head>
<body>
  <section class="card card--front" aria-label="Business card front">
    <div class="front__brand">Q7 Harbor</div>
    <ul class="front__contacts">
      <li>
        <svg viewBox="0 0 24 24" fill="#fff" aria-hidden="true"><path d="M6.6 10.8a15 15 0 0 0 6.6 6.6l2.2-2.2c.3-.3.7-.4 1-.2 1.1.4 2.3.6 3.6.6.6 0 1 .4 1 1V20c0 .6-.4 1-1 1A17 17 0 0 1 3 4c0-.6.4-1 1-1h3.5c.6 0 1 .4 1 1 0 1.3.2 2.5.6 3.6.1.3 0 .7-.2 1z"/></svg>
        1-800-555-0147
      </li>
      <li>
        <svg viewBox="0 0 24 24" fill="none" stroke="#fff" stroke-width="2" aria-hidden="true"><rect x="2" y="5" width="20" height="14"/><path d="M2 5l10 8 10-8"/></svg>
        info@q7harbor.net
      </li>
      <li>
        <svg viewBox="0 0 24 24" fill="none" stroke="#fff" stroke-width="1.6" aria-hidden="true"><circle cx="12" cy="12" r="10"/><ellipse cx="12" cy="12" rx="4.5" ry="10"/><path d="M2 12h20M4 7h16M4 17h16"/></svg>
        www.q7harbor.net
      </li>
      <li>
        <svg viewBox="0 0 24 24" aria-hidden="true"><rect x="3" y="3" width="18" height="18" rx="3" fill="#fff"/></svg>
        @q7-harbor-solutions-inc
      </li>
    </ul>
    <div class="front__person">
      <div class="person__name">JOHN DOE</div>
      <div class="person__role">CEO | FOUNDER</div>
    </div>
  </section>

  <section class="card card--back" aria-label="Business card back">
    <div class="back__brand"><span class="back__dot"></span>Q7 Harbor</div>
    <div class="back__statements">
      <p class="statement--vision">Helping businesses create workplaces where people love to work</p>
      <p class="statement--mission">Create the best remote work experience for people and companies</p>
    </div>
  </section>
</body>
</html>
```